" Trata-se de consultório médico particular, de especialidade em gastroenterologia, cujos impressos serao utilizados como cartao de visita, receituários e envelopes. "

```html
<!DOCTYPE html>
<html lang="pt-BR">
<head>
<meta charset="UTF-8">
<title>Papel timbrado — Helena Vasconti Ramos, Gastroenterologia</title>
<link rel="stylesheet" href="https://fonts.googleapis.com/css2?family=Cinzel:wght@400&family=Lato:wght@400&display=swap">
<style>
  :root {
    --backdrop: #ecebef;
    --paper: #ffffff;
    --brand: #7b68a6;
    --brand-soft: #e4e0ef;
    --ink-muted: #8a7fa8;
  }
  html, body {
    margin: 0;
    width: 1200px;
    height: 1200px;
    overflow: hidden;
    background: var(--backdrop);
  }
  .letterhead {
    position: absolute;
    left: 220px;
    top: 62px;
    width: 760px;
    height: 1075px;
    background: var(--paper);
    overflow: hidden;
    box-shadow: 0 2px 10px rgba(60, 50, 90, 0.12);
  }
  .brand {
    position: absolute;
    top: 96px;
    left: 0;
    right: 0;
    text-align: center;
    color: var(--brand);
  }
  .brand-name {
    font-family: "Cinzel", serif;
    font-weight: 400;
    font-size: 25px;
    letter-spacing: 1px;
    margin: 0;
    display: inline-flex;
    align-items: center;
    gap: 12px;
  }
  .brand-dot {
    width: 10px;
    height: 10px;
    border-radius: 50%;
    background: var(--brand);
  }
  .brand-specialty {
    font-family: "Lato", sans-serif;
    font-size: 13px;
    letter-spacing: 1.5px;
    margin: 4px 0 0;
    padding-left: 48px;
  }
  .footer-accent {
    position: absolute;
    left: 40px;
    bottom: 60px;
  }
  .contact {
    position: absolute;
    right: 52px;
    bottom: 58px;
    margin: 0;
    font-family: "Lato", sans-serif;
    font-style: normal;
    font-size: 12.5px;
    line-height: 1.6;
    color: var(--ink-muted);
    text-align: left;
  }
  .contact-phone {
    color: var(--brand);
    font-size: 14px;
    margin-bottom: 8px;
    display: block;
  }
</style>
</head>
<body>
  <main class="letterhead">
    <header class="brand">
      <h1 class="brand-name"><span class="brand-dot"></span>Helena Vasconti Ramos</h1>
      <p class="brand-specialty">Gastroenterologia</p>
    </header>

    <svg class="footer-accent" width="280" height="280" viewBox="0 0 280 280" aria-hidden="true">
      <circle cx="140" cy="140" r="120" fill="var(--brand-soft)" />
    </svg>

    <address class="contact">
      <span class="contact-phone">(27) 3014-5820</span>
      Rua das Acácias, 480<br>
      Ed. Monte Claro, sala 210<br>
      Jardim Europa, Vitória-ES<br>
      CEP 29050-120
    </address>
  </main>
</body>
</html>
```